Oven Cleaning Business owner needs business card design

Hi there,
Would like for a business card to be designed for myself, the owner of a professional oven cleaning business on the Sunshine Coast.
Would like it to look sleek, and modern-ish. Bit creative is encouraged too.
Include following:
Name/title: Corin ter Haghe, Owner
Phone number: 1300 482 916
Email: info@hearthshinecrew.com.au
Website: www.hearthshinecrew.com.au

```html
<!DOCTYPE html>
<html lang="en">
<head>
<meta charset="utf-8">
<title>Hearthshine Crew — Business Card</title>
<link rel="stylesheet" href="https://fonts.googleapis.com/css2?family=Lato:wght@400;700;900&display=swap">
<style>
  :root {
    --bg: #cfd0d1;
    --card: #ffffff;
    --teal: #4fc3cb;
    --ink: #111111;
    --muted: #2a2a2a;
  }
  * { box-sizing: border-box; margin: 0; padding: 0; }
  html, body { width: 1200px; height: 900px; overflow: hidden; }
  body {
    background: var(--bg);
    font-family: "Lato", sans-serif;
    position: relative;
  }
  .card {
    position: absolute;
    left: 300px;
    width: 600px;
    height: 343px;
    background: var(--card);
    border-radius: 22px;
    box-shadow: 0 6px 18px rgba(0,0,0,0.18);
  }
  .card--front { top: 70px; }
  .card--back { top: 487px; }

  .brand {
    position: absolute;
    display: flex;
    align-items: center;
    gap: 18px;
  }
  .card--front .brand { left: 50%; top: 50%; transform: translate(-50%, -50%); }
  .card--back .brand { left: 50%; top: 48px; transform: translateX(-50%); }
  .brand__dot {
    width: 58px; height: 58px;
    border-radius: 50%;
    background: var(--teal);
    flex: none;
  }
  .brand__name {
    font-weight: 900;
    font-size: 46px;
    letter-spacing: 1px;
    color: var(--ink);
    white-space: nowrap;
  }

  .owner {
    position: absolute;
    right: 318px;
    top: 206px;
    text-align: right;
  }
  .owner__name {
    font-size: 30px;
    font-weight: 400;
    color: var(--teal);
    line-height: 1.1;
  }
  .owner__title {
    font-size: 15px;
    color: var(--muted);
    margin-top: 4px;
  }
  .divider {
    position: absolute;
    left: 296px;
    top: 196px;
    width: 2px;
    height: 86px;
    background: var(--teal);
  }
  .contacts {
    position: absolute;
    left: 316px;
    top: 200px;
    list-style: none;
  }
  .contacts li {
    display: flex;
    align-items: center;
    gap: 8px;
    font-size: 14.5px;
    color: var(--ink);
    line-height: 26px;
  }
  .contacts svg { width: 14px; height: 14px; fill: var(--teal); flex: none; }
</style>
</head>
<body>
  <section class="card card--front">
    <div class="brand">
      <span class="brand__dot"></span>
      <span class="brand__name">Hearthshine Crew</span>
    </div>
  </section>

  <section class="card card--back">
    <div class="brand">
      <span class="brand__dot"></span>
      <span class="brand__name">Hearthshine Crew</span>
    </div>

    <div class="owner">
      <p class="owner__name">Corin ter Haghe</p>
      <p class="owner__title">Owner</p>
    </div>

    <div class="divider"></div>

    <ul class="contacts">
      <li>
        <svg viewBox="0 0 16 16" aria-hidden="true"><path d="M3.6 1.2l2.3 2.6-1.2 1.8c.9 2 2.4 3.6 4.5 4.6l1.8-1.2 2.7 2.2-1.2 2.6C7.2 14 2 8.8 1.1 2.4z"/></svg>
        1300 482 916
      </li>
      <li>
        <svg viewBox="0 0 16 16" aria-hidden="true"><path d="M1 3h14v10H1z M1.8 3.6L8 8.6l6.2-5" fill="none" stroke="#4fc3cb" stroke-width="1.6"/></svg>
        info@hearthshinecrew.com.au
      </li>
      <li>
        <svg viewBox="0 0 16 16" aria-hidden="true"><circle cx="8" cy="8" r="6.6" fill="none" stroke="#4fc3cb" stroke-width="1.4"/><path d="M1.4 8h13.2M8 1.4c-3.4 3.6-3.4 9.6 0 13.2M8 1.4c3.4 3.6 3.4 9.6 0 13.2" fill="none" stroke="#4fc3cb" stroke-width="1.2"/></svg>
        www.hearthshinecrew.com.au
      </li>
    </ul>
  </section>
</body>
</html>
```